Ledgrix Business Card

We need a business card design using the attached logo. The company is a financial services company that provides a dashboard (chart based information) for Executives of small businesses to use to better manage their information. The design must be progressive, make good utilization of the logo and project stability and financial security.

Industry/Entity Type

Financial

```html
<!DOCTYPE html>
<html lang="en">
<head>
<meta charset="utf-8">
<title>Ledgrix Business Card</title>
<link rel="stylesheet" href="https://fonts.googleapis.com/css2?family=Nunito+Sans:wght@400;700;800&display=swap">
<style>
  :root {
    --brand-red: #9b1b1e;
    --ink: #111111;
    --paper: #ffffff;
  }
  html, body {
    margin: 0;
    padding: 0;
    overflow: hidden;
    background: var(--paper);
  }
  .card {
    position: relative;
    width: 1050px;
    height: 1200px;
    overflow: hidden;
    background: var(--paper);
    font-family: "Nunito Sans", Arial, sans-serif;
    color: var(--ink);
  }
  .hero {
    position: absolute;
    left: 0;
    top: 0;
    width: 1050px;
    height: 600px;
    background: var(--brand-red);
    display: flex;
    align-items: center;
    justify-content: center;
  }
  .brand {
    display: flex;
    align-items: center;
    gap: 30px;
  }
  .brand-square {
    display: block;
    flex: none;
  }
  .brand-name {
    font-weight: 800;
    line-height: 1;
    letter-spacing: -1px;
  }
  .hero .brand-square {
    width: 150px;
    height: 150px;
    border: 14px solid var(--paper);
    box-sizing: border-box;
  }
  .hero .brand-name {
    font-size: 150px;
    color: var(--paper);
  }
  .contact {
    position: absolute;
    left: 46px;
    top: 650px;
    font-size: 26px;
    line-height: 1;
  }
  .contact-name {
    font-size: 29px;
    font-weight: 700;
    margin: 0 0 14px;
  }
  .contact-title {
    margin: 0 0 35px;
  }
  .contact-lines {
    list-style: none;
    margin: 0 0 30px;
    padding: 0;
  }
  .contact-lines li {
    display: flex;
    height: 41.5px;
  }
  .contact-label {
    width: 46px;
    font-weight: 700;
    font-size: 28px;
  }
  .address {
    font-style: normal;
  }
  .address span {
    display: block;
    height: 42px;
  }
  .address .website {
    margin-top: 6px;
  }
  .footer-brand {
    position: absolute;
    left: 490px;
    top: 1005px;
    gap: 20px;
  }
  .footer-brand .brand-square {
    width: 100px;
    height: 100px;
    border: 10px solid var(--brand-red);
    box-sizing: border-box;
  }
  .footer-brand .brand-name {
    font-size: 104px;
    color: var(--ink);
  }
</style>
</head>
<body>
  <main class="card">
    <header class="hero">
      <div class="brand">
        <span class="brand-square"></span>
        <span class="brand-name">Ledgrix</span>
      </div>
    </header>

    <section class="contact">
      <h1 class="contact-name">Name Of Employee</h1>
      <p class="contact-title">Job Title</p>
      <ul class="contact-lines">
        <li><span class="contact-label">t</span><span>Telephone No.</span></li>
        <li><span class="contact-label">f</span><span>Fax No.</span></li>
        <li><span class="contact-label">m</span><span>Mobile No.</span></li>
        <li><span class="contact-label">e</span><span>Email Address</span></li>
      </ul>
      <address class="address">
        <span>Office</span>
        <span>Address Line 1</span>
        <span>Address Line 2</span>
        <span>City &amp; Postcode</span>
        <span class="website">Website</span>
      </address>
    </section>

    <div class="brand footer-brand">
      <span class="brand-square"></span>
      <span class="brand-name">Ledgrix</span>
    </div>
  </main>
</body>
</html>
```